I need to have a website created  for my company , Tulip Dash.  What we are selling is mini electric trucks . These mini electric trucks require no license
or insurance.  They only go 25 k/h and are considered to be electric  mobility covered  scooters .  So far i only have a dozen of these just to see how well they sell before i sink a bunch of money into other models , designs ect. I am submitting 5 or 6 pics of the model to be put on the website along with one pic containing the specs of  the model i am going to sell .  Tulip Dash is the name of the company with our catch phrase : Savor the open road with a tulip dash.  The consumers i would like to target mostly are people who are unable to get a  drivers license .  It would give seniors who have had their license taken away for medical reasons,  age etc. Anyone who does not have the luxury of having a car  but still need to do life tasks like going to grocery store ,  dr appt  but have to rely on someone else to take them . This scooter gives them that freedom to get where they want whenever they want to keep their independence at an affordable price.  The web domain i already have is at www.tulipdash-example.ca  i will also include a pic of my business cards that contains all the info of the company eg. Phone number , email etc. Thank you for you time and creativity

```html
<!DOCTYPE html>
<html lang="en">
<head>
<meta charset="utf-8">
<title>Tulip Dash — Website Design</title>
<link rel="stylesheet" href="https://fonts.googleapis.com/css2?family=Catamaran:wght@400;500;600;700;800&family=Heebo:wght@400;500;700&display=swap">
<style>
:root{
  --red:#e0040b;
  --red-dark:#b80008;
  --black:#0b0b0b;
  --charcoal:#333;
  --board:#e3e3e3;
  --light:#f2f2f2;
  --white:#fff;
  --text:#222;
  --muted:#6b6b6b;
  --photo-gray:linear-gradient(160deg,#e9e9e9,#bdbdbd);
}
*{margin:0;padding:0;box-sizing:border-box}
html,body{width:1200px;height:1200px;overflow:hidden}
body{background:var(--board);font-family:"Heebo",sans-serif;color:var(--text);position:relative}
.abs{position:absolute}
.page{position:absolute;background:var(--white);overflow:hidden;box-shadow:0 4px 18px rgba(0,0,0,.08)}
.page-home{left:60px;top:60px;width:514px;height:1140px}
.page-lower{left:628px;top:0;width:514px;height:962px}

/* brand */
.brand{display:flex;align-items:center;gap:5px;font-family:"Catamaran",sans-serif;font-weight:800;text-transform:uppercase;line-height:.9}
.brand-dot{width:10px;height:10px;border-radius:50%;background:var(--red)}
.brand-name{font-size:11px;color:var(--black)}

/* nav */
.nav{left:258px;top:29px;display:flex;gap:15px;font-size:6.5px;text-transform:uppercase;color:var(--black)}

/* hero */
.hero-title{left:42px;top:82px;width:220px;z-index:2;font-family:"Catamaran",sans-serif;font-weight:500;font-size:27px;line-height:33px;text-transform:uppercase;color:var(--black);white-space:nowrap}
.hero-title em{font-style:normal;font-weight:800;color:var(--red)}
.btn{background:var(--red);color:var(--white);border-radius:20px;font-family:"Catamaran",sans-serif;font-weight:700;display:flex;align-items:center;justify-content:center}
.btn-hero{left:43px;top:202px;width:158px;height:35px;font-size:11px}
.btn-small{width:64px;height:21px;font-size:6px;text-transform:uppercase}
.photo{background:var(--photo-gray)}
.hero-photo{left:272px;top:66px;width:212px;height:140px;border-radius:6px}
.hero-model{left:366px;top:196px;font-family:"Catamaran",sans-serif;font-weight:600;font-size:17px;color:var(--white)}

/* model cards */
.card{top:313px;width:118px;height:180px;border:1.5px solid var(--black);background:var(--white);text-align:center}
.card--featured{border-color:var(--red)}
.card-photo{margin:12px 6px 0;height:78px;border-radius:4px}
.card-name{font-family:"Catamaran",sans-serif;font-weight:600;font-size:17px;line-height:15px;color:var(--red);margin-top:20px}
.card-text{font-size:5.5px;line-height:8px;color:var(--muted);margin:6px 12px 0}
.tag{left:252px;top:304px;width:58px;height:9px;background:var(--red);color:var(--white);font-size:5.5px;font-weight:700;display:flex;align-items:center;justify-content:center;text-transform:uppercase}

/* freedom band */
.freedom{left:0;top:546px;width:514px;height:256px;overflow:hidden}
.freedom-photo{left:0;top:0;width:514px;height:256px;background:linear-gradient(120deg,#4f6b78,#9aa9ae 40%,#2c3b44)}
.freedom-title{left:216px;top:586px;width:290px;text-align:center;font-family:"Catamaran",sans-serif;font-weight:800;font-size:36px;line-height:37px;color:var(--white);text-transform:uppercase}
.freedom-title span{font-weight:600}
.freedom-copy{left:262px;top:672px;width:200px;font-size:7.3px;line-height:10.8px;color:var(--white)}
.freedom-copy p+p{margin-top:7px}

/* best seller */
.seller-photo{width:156px;height:176px;border-radius:8px;background:linear-gradient(180deg,#f4f4f4,#cfcfcf)}
.eyebrow{font-family:"Catamaran",sans-serif;font-weight:800;font-size:10px;color:var(--red);text-transform:uppercase}
.seller-title{font-family:"Catamaran",sans-serif;font-weight:800;font-size:28px;line-height:28px;color:var(--black);white-space:nowrap}
.seller-copy{width:230px;font-size:6px;line-height:8.8px;color:var(--muted)}
.features{display:grid;grid-template-columns:86px 140px;row-gap:10px;font-family:"Catamaran",sans-serif;font-weight:600;font-size:7.5px;color:var(--black)}
.feature{display:flex;align-items:center;gap:5px}
.feature i{display:block;width:11px;height:11px;background:var(--red);border-radius:2px}

/* service */
.band-black{background:var(--black);overflow:hidden}
.svc-head{display:flex;align-items:center;gap:10px}
.svc-mark{width:34px;height:34px;border-radius:50%;background:var(--red)}
.svc-eyebrow{font-family:"Catamaran",sans-serif;font-weight:500;font-size:13px;line-height:13px;color:var(--white);text-transform:uppercase}
.svc-title{font-family:"Catamaran",sans-serif;font-weight:800;font-size:29px;line-height:28px;color:var(--white);text-transform:uppercase}
.svc-card{width:169px;height:207px;background:var(--white);box-shadow:0 4px 14px rgba(0,0,0,.1)}
.svc-photo{height:102px}
.svc-label{height:26px;background:var(--red);color:var(--white);font-family:"Catamaran",sans-serif;font-weight:700;font-size:13px;padding-left:22px;display:flex;align-items:center}
.svc-text{font-size:5.8px;line-height:8.8px;color:var(--muted);margin:12px 20px 0}
.svc-link{font-size:6px;font-weight:700;color:var(--red);margin:7px 20px 0;text-transform:uppercase}

/* help */
.help{left:0;top:688px;width:514px;height:116px;background:var(--red);overflow:hidden}
.help-photo{left:52px;top:640px;width:152px;height:164px;border-radius:70px 70px 0 0;background:linear-gradient(180deg,#b9a08a,#7b7b7b 55%,#6d6d6d)}
.help-title{left:223px;top:704px;font-family:"Catamaran",sans-serif;font-weight:700;font-size:16px;color:var(--white);text-transform:uppercase}
.help-copy{left:223px;top:728px;width:206px;font-size:6px;line-height:9px;color:var(--white)}
.help-phone{left:223px;top:764px;display:flex;align-items:center;gap:6px;font-family:"Catamaran",sans-serif;font-weight:600;font-size:17px;color:var(--white)}
.phone-icon{width:16px;height:16px;border-radius:50%;background:var(--black);display:flex;align-items:center;justify-content:center}

/* footer */
.footer{left:0;top:804px;width:514px;height:158px;background:var(--black)}
.footer-blurb{left:126px;top:872px;width:120px;font-size:5.8px;line-height:8.5px;color:#cfcfcf}
.footer-col{top:830px;font-size:6px;line-height:13.6px;color:var(--white)}
.footer-col h4{font-family:"Catamaran",sans-serif;font-size:7.5px;font-weight:700;margin-bottom:1px}
.footer-rule{left:126px;top:924px;width:264px;height:1px;background:#555}
.footer-copy{left:126px;top:938px;font-size:5px;color:#cfcfcf}
.social{left:304px;top:939px;display:flex;gap:17px}
.social i{display:block;width:7px;height:7px;border-radius:50%;background:var(--white)}

/* top strip */
.strip{left:0;top:0;width:514px;height:40px;background:#2a2a2a;overflow:hidden}

/* master brand */
.master-brand{left:736px;top:1022px;display:flex;align-items:center;gap:18px}
.master-brand .brand-dot{width:84px;height:84px}
.master-brand .brand-name{font-family:"Catamaran",sans-serif;font-weight:800;font-size:52px;line-height:42px;color:var(--red);text-transform:uppercase}
</style>
</head>
<body>

<!-- Home page -->
<section class="page page-home">
  <svg class="abs" style="left:0;top:0" width="514" height="264" aria-hidden="true">
    <polygon points="300,0 514,0 514,264 170,264" fill="#f2f2f2"/>
  </svg>
  <div class="abs brand" style="left:38px;top:18px"><span class="brand-dot"></span><span class="brand-name">Tulip<br>Dash</span></div>
  <nav class="abs nav"><span>Home</span><span>About us</span><span>Mini trucks</span><span>Blog</span><span>Contact</span></nav>
  <div class="abs photo hero-photo" role="img" aria-label="White mini electric pickup truck with roof lights, three-quarter front view"></div>
  <h1 class="abs hero-title">Savor the open<br>road with a<br><em>tulip dash</em></h1>
  <div class="abs btn btn-hero">See Mini E-Truck models</div>
  <svg class="abs" style="left:312px;top:170px" width="202" height="56" aria-hidden="true">
    <polygon points="30,0 202,0 202,56 0,56" fill="#e0040b"/>
  </svg>
  <div class="abs hero-model">MiniTruck XYZ10</div>

  <div class="abs tag">High demand</div>
  <article class="abs card" style="left:60px">
    <div class="photo card-photo" role="img" aria-label="Mini electric truck MiniTruck XYZ10"></div>
    <h3 class="card-name">MiniTruck<br>XYZ10</h3>
    <p class="card-text">A compact electric runabout for daily errands around town</p>
  </article>
  <article class="abs card card--featured" style="left:194px">
    <div class="photo card-photo" role="img" aria-label="Mini electric truck MiniTruck ABC20"></div>
    <h3 class="card-name">MiniTruck<br>ABC20</h3>
    <p class="card-text">Our most requested model with extra cargo room at the back</p>
  </article>
  <article class="abs card" style="left:327px">
    <div class="photo card-photo" role="img" aria-label="Mini electric truck MiniTruck QRT40"></div>
    <h3 class="card-name">MiniTruck<br>QRT40</h3>
    <p class="card-text">Quiet, steady and simple to drive, no licence required</p>
  </article>

  <div class="abs freedom">
    <div class="abs freedom-photo" role="img" aria-label="Smiling senior man driving a vehicle, hands on the wheel"></div>
    <svg class="abs" style="left:0;top:0" width="514" height="256" aria-hidden="true">
      <polygon points="308,0 514,0 514,256 188,256" fill="#e0040b"/>
    </svg>
  </div>
  <h2 class="abs freedom-title"><span>Freedom</span> with<br>Tulip Dash</h2>
  <div class="abs freedom-copy">
    <p>Get to the grocery store, the doctor or a friend's place whenever you choose. Our mini electric trucks top out at 25 km/h and are classed as mobility scooters, so no driver's licence or insurance is needed.</p>
    <p>Keep your independence at an affordable price and stop waiting on someone else for a ride.</p>
  </div>

  <div class="abs seller-photo" style="left:52px;top:844px" role="img" aria-label="Mini electric truck DF100, front view"></div>
  <div class="abs eyebrow" style="left:239px;top:852px">Best seller</div>
  <h2 class="abs seller-title" style="left:238px;top:866px">MiniTruck DF100</h2>
  <p class="abs seller-copy" style="left:239px;top:901px">Our best seller pairs a roomy cab with a practical cargo bed and a range that covers a full day of errands on one charge.</p>
  <div class="abs features" style="left:239px;top:941px">
    <span class="feature"><i></i>Quiet motor</span><span class="feature"><i></i>Charges from a home outlet</span>
    <span class="feature"><i></i>Safe at 25 km/h</span><span class="feature"><i></i>Roomy bed</span>
  </div>
  <div class="abs btn btn-small" style="left:236px;top:994px">Buy now</div>

  <div class="abs band-black" style="left:0;top:1064px;width:514px;height:76px">
    <svg class="abs" style="left:0;top:0" width="514" height="76" aria-hidden="true">
      <polygon points="410,0 514,0 514,76 370,76" fill="#333"/>
    </svg>
    <div class="abs svc-head" style="left:168px;top:26px">
      <span class="svc-mark"></span>
      <div><div class="svc-eyebrow">Top quality</div><div class="svc-title">Serivce</div></div>
    </div>
  </div>
</section>

<!-- Lower page -->
<section class="page page-lower">
  <div class="abs strip">
    <svg class="abs" style="left:0;top:0" width="514" height="40" aria-hidden="true">
      <polygon points="200,0 514,0 514,40 188,40" fill="#e0040b"/>
    </svg>
  </div>

  <div class="abs seller-photo" style="left:52px;top:76px" role="img" aria-label="Mini electric truck DF100, front view"></div>
  <div class="abs eyebrow" style="left:239px;top:86px">Best seller</div>
  <h2 class="abs seller-title" style="left:238px;top:100px">MiniTruck DF100</h2>
  <p class="abs seller-copy" style="left:239px;top:139px">Our best seller pairs a roomy cab with a practical cargo bed and a range that covers a full day of errands on one charge.</p>
  <div class="abs features" style="left:239px;top:178px">
    <span class="feature"><i></i>Quiet motor</span><span class="feature"><i></i>Charges from a home outlet</span>
    <span class="feature"><i></i>Safe at 25 km/h</span><span class="feature"><i></i>Roomy bed</span>
  </div>
  <div class="abs btn btn-small" style="left:236px;top:230px">Buy now</div>

  <div class="abs band-black" style="left:0;top:300px;width:514px;height:234px">
    <svg class="abs" style="left:0;top:0" width="514" height="234" aria-hidden="true">
      <polygon points="410,34 514,34 514,234 330,234" fill="#333"/>
    </svg>
    <div class="abs svc-head" style="left:168px;top:30px">
      <span class="svc-mark"></span>
      <div><div class="svc-eyebrow">Top quality</div><div class="svc-title">Serivce</div></div>
    </div>
  </div>
  <article class="abs svc-card" style="left:80px;top:406px">
    <div class="svc-photo" style="background:linear-gradient(160deg,#8a96a8,#2e3f63)" role="img" aria-label="Mechanic in overalls working under a raised vehicle"></div>
    <div class="svc-label">Expert mechanics</div>
    <p class="svc-text">Trained technicians keep your truck running smoothly, with quick checkups and repairs done right the first time.</p>
    <div class="svc-link">Learn more</div>
  </article>
  <article class="abs svc-card" style="left:270px;top:406px">
    <div class="svc-photo" style="background:linear-gradient(160deg,#9fb0c6,#4a5160)" role="img" aria-label="Happy driver seated behind the wheel of a vehicle"></div>
    <div class="svc-label">Highly Supportive</div>
    <p class="svc-text">Our friendly team answers every question, from the first test drive to charging tips and everyday care.</p>
    <div class="svc-link">Learn more</div>
  </article>

  <div class="abs help">
    <svg class="abs" style="left:0;top:0" width="514" height="116" aria-hidden="true">
      <polygon points="480,20 514,20 514,116 430,116" fill="#b80008"/>
    </svg>
  </div>
  <div class="abs help-photo" role="img" aria-label="Cheerful grey-haired man in a t-shirt giving a thumbs up"></div>
  <div class="abs help-title">Need help?</div>
  <p class="abs help-copy">Not sure which model fits your needs? Give us a call and we will gladly walk you through your options.</p>
  <div class="abs help-phone">
    <span class="phone-icon"><svg width="9" height="9" viewBox="0 0 24 24" aria-hidden="true"><path fill="#e0040b" d="M6.6 10.8a15 15 0 0 0 6.6 6.6l2.2-2.2a1 1 0 0 1 1-.25 11.4 11.4 0 0 0 3.6.57 1 1 0 0 1 1 1V20a1 1 0 0 1-1 1A17 17 0 0 1 3 4a1 1 0 0 1 1-1h3.5a1 1 0 0 1 1 1c0 1.250.2 2.45.57 3.57a1 1 0 0 1-.25 1z"/></svg></span>
    +1 555 014 2290
  </div>

  <footer class="abs footer"></footer>
  <div class="abs brand" style="left:126px;top:832px"><span class="brand-dot"></span><span class="brand-name" style="color:#fff">Tulip<br>Dash</span></div>
  <p class="abs footer-blurb">Mini electric trucks for life's everyday trips.</p>
  <div class="abs footer-col" style="left:273px">
    <h4>Company</h4><div>About us</div><div>Services</div><div>Our offerings</div><div>Blog</div><div>Careers</div>
  </div>
  <div class="abs footer-col" style="left:354px">
    <h4>E-Trucks</h4><div>ABC120</div><div>DEF240</div><div>PQR460</div><div>MNO990</div>
  </div>
  <div class="abs footer-rule"></div>
  <div class="abs footer-copy">© 2022 Tulip Dash</div>
  <div class="abs social" aria-label="Social links"><i></i><i></i><i></i><i></i></div>
</section>

<!-- Brand mark -->
<div class="abs master-brand">
  <span class="brand-dot"></span>
  <span class="brand-name">Tulip<br>Dash</span>
</div>

</body>
</html>
```